Holvern Incorporated

Holvern is a business that provides consulting, and manages and supplies trades persons in the construction and heavy industries sector. We build, do maintenance, install machinery, and can manage projects or jobs. Would like or prefer more clean, classic designs. Blacks/greys, but open to almost anything.

Target Market(s)

Industrial/Construction/Manufacturing

Industry/Entity Type

Construction Company

Contact Information for Business Card

Clean, business name on the front, possibly have the details on the back, but open to any ideas.

Logo Text

We currently do not have a slogan, open to ideas

Font styles to use
Serif
Sans Serif

Colors

Designer to choose colors to be used in the design.

Requirements
Should not have
• the oval is not my logo, was just an idea. please don't send 20 designs with the oval

```html
<!DOCTYPE html>
<html lang="en">
<head>
<meta charset="utf-8">
<title>Holvern Incorporated — Business Card</title>
<link rel="stylesheet" href="https://fonts.googleapis.com/css2?family=Arimo:wght@400;700&family=Libre+Baskerville:wght@700&display=swap">
<style>
  :root {
    --backdrop: #c9c9c9;
    --card-dark: #000000;
    --card-light: #ffffff;
    --ink: #111111;
    --ink-soft: #222222;
  }
  * { box-sizing: border-box; margin: 0; padding: 0; }
  html, body {
    width: 1200px; height: 900px; overflow: hidden;
    background: var(--backdrop);
  }
  .canvas { position: relative; width: 1200px; height: 900px; }

  .card {
    position: absolute;
    width: 560px; height: 320px;
    border-radius: 26px;
    box-shadow: 0 6px 18px rgba(0,0,0,0.18);
  }
  .card--front { left: 80px; top: 110px; background: var(--card-dark); }
  .card--back  { left: 560px; top: 470px; background: var(--card-light); color: var(--ink); }

  .wordmark {
    font-family: "Libre Baskerville", Georgia, serif;
    font-weight: 700;
    line-height: 1;
    text-align: center;
  }
  .wordmark__name { display: block; font-size: 58px; letter-spacing: 1px; }
  .wordmark__suffix { display: block; font-size: 11px; letter-spacing: 3px; text-transform: uppercase; margin-top: 8px; }

  .card--front .wordmark {
    position: absolute; left: 0; right: 0; top: 118px;
    color: var(--card-light);
  }
  .card--back .wordmark {
    position: absolute; left: 40px; width: 300px; top: 40px;
    color: var(--ink);
  }
  .card--back .wordmark__name { font-size: 48px; }

  .contact {
    position: absolute; left: 34px; bottom: 30px;
    font-family: Arimo, Arial, sans-serif;
    color: var(--ink-soft);
  }
  .contact__name { font-size: 19px; font-weight: 700; text-transform: uppercase; letter-spacing: 0.5px; }
  .contact__role { font-size: 16px; margin-bottom: 8px; }
  .contact__list { list-style: none; font-size: 16px; line-height: 1.3; }
  .contact__list li { display: flex; align-items: center; gap: 8px; }
  .contact__list svg { width: 13px; height: 13px; fill: var(--ink-soft); flex: none; }

  .address {
    position: absolute; right: 34px; top: 170px;
    font-family: Arimo, Arial, sans-serif;
    font-size: 16px; line-height: 1.3; text-align: right;
    color: var(--ink-soft);
  }
</style>
</head>
<body>
<main class="canvas">
  <section class="card card--front" aria-label="Card front">
    <div class="wordmark">
      <span class="wordmark__name">Holvern</span>
      <span class="wordmark__suffix">Incorporated</span>
    </div>
  </section>

  <section class="card card--back" aria-label="Card back">
    <div class="wordmark">
      <span class="wordmark__name">Holvern</span>
      <span class="wordmark__suffix">Incorporated</span>
    </div>

    <div class="contact">
      <p class="contact__name">Daniel Harwick</p>
      <p class="contact__role">Managing Director</p>
      <ul class="contact__list">
        <li>
          <svg viewBox="0 0 16 16" aria-hidden="true"><path d="M2 5c0-2 2-3 6-3s6 1 6 3v1h-3V5H5v1H2zM4 7h8l2 6H2z"/></svg>
          044-555 018 274
        </li>
        <li>
          <svg viewBox="0 0 16 16" aria-hidden="true"><path d="M1 3h14v10H1zM2 4l6 5 6-5v1L8 10 2 5z" fill-rule="evenodd"/></svg>
          info@holvern.co
        </li>
        <li>
          <svg viewBox="0 0 16 16" aria-hidden="true"><circle cx="8" cy="8" r="7"/></svg>
          www.holvern.co
        </li>
      </ul>
    </div>

    <address class="address">
      18, Foundry Lane<br>
      Northmere, 30716
    </address>
  </section>
</main>
</body>
</html>
```